Thumbnail for "Exclusive Shows"

I need a Thumbnail / Cover for exclusive shows I'll upload to sonawharf. It should be unique and especially made for this purpose. My channel delivers electronic dance music and thus should be seen in the thumbnail / cover. There will be now attached files so there is nothing to influence you in your work.

Target Market(s)

Young people enjoying electronic dance music

Colors
e667a6
876aae
f04a50
f68d4d
33a6d7
3176b5

Requirements
Must have
• The design should include my logo (which will be the only thing provided later this day).
Nice to have
• Would it be good to keep it simple with texting. If you want to integrate the word "Exclusive" or "Exclusive Show" it will fit as long as it's fit to the whole design.

```html
<!DOCTYPE html>
<html lang="en">
<head>
<meta charset="utf-8">
<title>Velvetrune – Exclusive Show Cover</title>
<link rel="stylesheet" href="https://fonts.googleapis.com/css2?family=Orbitron:wght@900&family=Questrial&display=swap">
<style>
  :root {
    --pink: #e667a6;
    --violet: #876aae;
    --red: #f04a50;
    --orange: #f68d4d;
    --sky: #33a6d7;
    --blue: #3176b5;
    --deep: #2a1f6e;
    --night: #1b1450;
    --logo-blue: #1496d8;
    --white: #ffffff;
    --band: rgba(40, 30, 90, 0.72);
    --chrome-light: #eef6ff;
    --chrome-mid: #8fb0d2;
    --chrome-dark: #3d5c82;
  }
  * { margin: 0; padding: 0; box-sizing: border-box; }
  html, body {
    width: 1200px; height: 1200px; overflow: hidden;
    background: var(--night);
  }
  .cover {
    position: relative; width: 1200px; height: 1200px; overflow: hidden;
    font-family: "Questrial", "Century Gothic", sans-serif;
  }
  .cover__art {
    position: absolute; inset: 0;
    background:
      radial-gradient(circle at 50% 52%, rgba(240, 74, 80, 0.55) 0, rgba(230, 103, 166, 0.35) 26%, transparent 48%),
      radial-gradient(circle at 50% 50%, transparent 44%, rgba(51, 166, 215, 0.55) 46%, transparent 50%),
      linear-gradient(90deg, rgba(51, 166, 215, 0.5) 0%, transparent 30%, transparent 70%, rgba(230, 103, 166, 0.55) 100%),
      linear-gradient(180deg, var(--blue) 0%, var(--violet) 30%, var(--deep) 60%, var(--violet) 85%, var(--pink) 100%);
  }
  .cover__graphics { position: absolute; inset: 0; }
  .brand-name {
    font-family: "Orbitron", sans-serif; font-weight: 900;
    fill: var(--white);
  }
  .headline {
    font-family: "Orbitron", sans-serif; font-weight: 900;
    fill: url(#chrome);
    stroke: var(--chrome-dark); stroke-width: 2;
  }
  .links {
    position: absolute; left: 0; top: 1000px; width: 1200px; height: 100px;
    background: var(--band);
    color: var(--white);
    display: flex; flex-direction: column; align-items: center; justify-content: center;
    gap: 8px;
  }
  .links__row { display: flex; align-items: center; gap: 26px; font-size: 23px; }
  .links__item { display: flex; align-items: center; gap: 10px; }
  .links__network { display: flex; align-items: center; gap: 6px; font-size: 15px; color: #e3e3ee; }
  .links__network::before {
    content: ""; width: 14px; height: 14px; border-radius: 50%;
    background: #e3e3ee; display: block;
  }
  .links__site { font-size: 21px; letter-spacing: 0.5px; }
</style>
</head>
<body>
  <main class="cover">
    <div class="cover__art" role="img" aria-label="Neon electronic music backdrop: glowing wireframe sound waves, concentric rings and layered triangles in blue, violet, pink and red"></div>

    <svg class="cover__graphics" width="1200" height="1200" viewBox="0 0 1200 1200">
      <defs>
        <linearGradient id="chrome" x1="0" y1="0" x2="0" y2="1">
          <stop offset="0" stop-color="var(--chrome-light)"/>
          <stop offset="0.45" stop-color="var(--chrome-mid)"/>
          <stop offset="0.55" stop-color="var(--chrome-dark)"/>
          <stop offset="1" stop-color="var(--chrome-light)"/>
        </linearGradient>
      </defs>

      <g class="brand-lockup">
        <rect class="brand-lockup__bar" x="219" y="363" width="781" height="12" fill="var(--logo-blue)"/>
        <text class="brand-name" x="610" y="466" text-anchor="middle" font-size="74" textLength="720" lengthAdjust="spacingAndGlyphs">VELVETRUNE</text>
        <rect class="brand-lockup__bar" x="219" y="486" width="781" height="12" fill="var(--logo-blue)"/>
      </g>

      <g class="headline-group">
        <text class="headline" x="600" y="652" text-anchor="middle" font-size="96" textLength="1000" lengthAdjust="spacingAndGlyphs">EXCLUSIVE</text>
        <text class="headline" x="600" y="772" text-anchor="middle" font-size="96" textLength="510" lengthAdjust="spacingAndGlyphs">SHOW</text>
      </g>
    </svg>

    <footer class="links">
      <div class="links__row">
        <span class="links__item"><span class="links__network">Friendra</span>/VelvetruneDJ</span>
        <span class="links__item"><span class="links__network">Chirpline</span>@velvetruneDJ</span>
        <span class="links__item"><span class="links__network">sonawharf</span>/velvetruneDJ</span>
        <span class="links__item"><span class="links__network">Tonecove</span>/velvet_rune</span>
      </div>
      <div class="links__site">WWW.velvet-rune.COM</div>
    </footer>
  </main>
</body>
</html>
```